Business Card Design

Recruitment Company. Want to keep the logo and the green colour

Industry/Entity Type

Business

Contact Information for Business Card

Hi,

1.)
MARTIN COLLARD
Director
Level 4, 238 Finch Terrace
Brisbane QLD 4000
M 0412 604 337
E martin@paceltalent.com.au
www.paceltalent.com.au

2.)
TOM WHITFORD
Director
Level 4, 238 Finch Terrace
Brisbane QLD 4000
M 0419 572 641
E tom@paceltalent.com.au

Want something different and eye catching, happy for you guys to use your design flare to work some magic with these.

Many Thanks
Tom

```html
<!DOCTYPE html>
<html lang="en">
<head>
<meta charset="utf-8">
<title>Pacel Talent – Business Cards</title>
<link rel="stylesheet" href="https://fonts.googleapis.com/css2?family=Ubuntu:wght@400;500;700&display=swap">
<style>
  :root {
    --page: #ece9e3;
    --card-white: #ffffff;
    --lime-light: #e6f4b8;
    --lime: #b8dd4e;
    --green: #5cb346;
    --green-deep: #3f9a3a;
    --ring-inner: #a6d23a;
    --text-green: #59ae3f;
    --muted-green: #6dba52;
  }
  * { box-sizing: border-box; margin: 0; padding: 0; }
  html, body {
    width: 1200px; height: 1000px; overflow: hidden;
    background: var(--page);
    font-family: "Ubuntu", sans-serif;
  }
  .stage { position: relative; width: 1200px; height: 1000px; }

  .card {
    position: absolute;
    width: 620px; height: 354px;
    overflow: hidden;
    box-shadow: 0 10px 30px rgba(0,0,0,0.18);
  }

  /* Front */
  .card--front {
    left: 290px; top: 70px;
    background: radial-gradient(ellipse at 55% 45%, var(--card-white) 20%, var(--lime-light) 55%, var(--lime) 100%);
  }
  .seal {
    position: absolute;
    border-radius: 50%;
    background: var(--card-white);
    border: 8px solid var(--green);
    box-shadow: inset 0 0 0 6px var(--ring-inner);
    display: flex; align-items: center; justify-content: center;
  }
  .card--front .seal {
    width: 330px; height: 330px;
    left: 145px; top: 12px;
  }

  .brand {
    display: flex; align-items: center; gap: 10px;
    color: var(--text-green);
    font-weight: 700;
    line-height: 1;
    white-space: nowrap;
  }
  .brand__dot {
    border-radius: 50%;
    background: var(--text-green);
    flex: none;
  }
  .card--front .brand { font-size: 44px; }
  .card--front .brand__dot { width: 26px; height: 26px; }

  /* Back */
  .card--back {
    left: 290px; top: 570px;
    background: linear-gradient(160deg, var(--card-white) 40%, var(--lime-light) 80%, #d6ee8a 100%);
  }
  .card--back .seal {
    width: 330px; height: 330px;
    left: 40px; top: -150px;
    align-items: flex-end;
    padding-bottom: 50px;
  }
  .card--back .brand { font-size: 36px; }
  .card--back .brand__dot { width: 22px; height: 22px; }

  .person {
    position: absolute;
    right: 34px; top: 150px;
    width: 250px;
    text-align: right;
  }
  .person__name {
    color: var(--text-green);
    font-size: 27px; font-weight: 700;
    padding-bottom: 8px;
    border-bottom: 2px solid var(--green);
    text-align: left;
  }
  .person__role {
    color: #4d8f35;
    font-size: 19px; font-weight: 700;
    margin-top: 6px;
  }

  .contact {
    position: absolute;
    left: 36px; bottom: 26px;
    list-style: none;
    color: var(--muted-green);
    font-size: 15px;
    line-height: 1.3;
  }
  .contact li { display: flex; }
  .contact__label { width: 26px; color: #557a3e; flex: none; }
</style>
</head>
<body>
<main class="stage">
  <section class="card card--front" aria-label="Card front">
    <div class="seal">
      <div class="brand"><span class="brand__dot"></span>pacel talent</div>
    </div>
  </section>

  <section class="card card--back" aria-label="Card back">
    <div class="seal">
      <div class="brand"><span class="brand__dot"></span>pacel talent</div>
    </div>

    <div class="person">
      <h1 class="person__name">Martin Collard</h1>
      <p class="person__role">Director</p>
    </div>

    <ul class="contact">
      <li><span class="contact__label">A:</span><span>Level 4, 238 Finch Terrace Brisbane<br>QLD 4000</span></li>
      <li><span class="contact__label">P:</span><span>0412 604 337</span></li>
      <li><span class="contact__label">E:</span><span>martin@paceltalent.com.au</span></li>
      <li><span class="contact__label">W:</span><span>www.paceltalent.com.au</span></li>
    </ul>
  </section>
</main>
</body>
</html>
```